full stationary design for a modern sleek design company

we are a design company that does modern minimalistic interior design works as well as other design services for high end clients.
we need a full stationary design including and not limited to (double sided business card, letter head, envelopes, documents folder...etc) that reflects the modern style design we do.
sleek modern and minimalistic is the requirements.
Updates

please use the latest attached files as there was a slight modification on the logo Added Wednesday, March 1, 2017

minor update on the logo files in JPG and PSD has been updated kindly follow the new attachments. Added Thursday, March 2, 2017

Target Market(s)

modern minimalist clients

Industry/Entity Type

Design Agency

Requirements
Must have
• the logo
Nice to have
• i like the colors in the colored 3D logo attached
Should not have
• too many colors

```html
<!DOCTYPE html>
<html lang="en">
<head>
<meta charset="utf-8">
<title>Linea Atelier – Business Card</title>
<link rel="stylesheet" href="https://fonts.googleapis.com/css2?family=Montserrat:wght@400;500;600;700&display=swap">
<style>
  :root {
    --stage: #e4e4e4;
    --card-dark: #4d4d4d;
    --card-dark-edge: #3f3f3f;
    --card-light: #ffffff;
    --ink: #3a3a3a;
    --accent: #f39220;
    --muted: #d9d9d9;
  }
  * { box-sizing: border-box; margin: 0; padding: 0; }
  html, body {
    width: 1200px; height: 718px; overflow: hidden;
    background: var(--stage);
    font-family: "Montserrat", sans-serif;
  }
  .canvas {
    position: relative; width: 1200px; height: 718px;
    display: flex; align-items: center; justify-content: center; gap: 50px;
  }
  .card {
    position: relative; width: 525px; height: 300px;
    box-shadow: 0 10px 24px rgba(0,0,0,0.18);
  }
  /* Front */
  .card-front {
    background: linear-gradient(135deg, var(--card-dark) 0%, var(--card-dark-edge) 100%);
    display: flex; flex-direction: column; align-items: center; justify-content: center;
  }
  .brand-mark {
    display: flex; align-items: center; gap: 14px;
  }
  .brand-mark .square {
    width: 34px; height: 34px; background: var(--accent);
  }
  .brand-mark .name {
    font-weight: 700; font-size: 58px; color: #ffffff; letter-spacing: 1px; line-height: 1;
  }
  .front-web {
    position: absolute; left: 0; right: 0; bottom: 58px;
    text-align: center; color: var(--muted); font-size: 11px; letter-spacing: 0.5px;
  }
  /* Back */
  .card-back { background: var(--card-light); color: var(--ink); }
  .brand-lockup {
    position: absolute; top: 38px; right: 36px; text-align: right;
  }
  .brand-lockup .title {
    font-weight: 700; font-size: 30px; letter-spacing: 1px; color: var(--ink); line-height: 1;
  }
  .brand-lockup .byline {
    margin-top: 6px; font-weight: 600; font-size: 13px; letter-spacing: 8.4px;
    color: var(--accent); margin-right: -8px;
  }
  .person { position: absolute; left: 40px; top: 122px; }
  .person .person-name { font-weight: 600; font-size: 16px; letter-spacing: 0.5px; }
  .person .person-name strong { font-weight: 700; }
  .person .role { margin-top: 3px; font-size: 11px; color: var(--accent); font-weight: 500; }
  .contact { position: absolute; right: 40px; bottom: 34px; width: 200px; font-size: 12px; font-weight: 500; line-height: 1.45; }
  .contact .address { margin-bottom: 12px; padding-left: 14px; }
  .contact .lines { border-left: 3px solid var(--accent); padding-left: 11px; }
</style>
</head>
<body>
  <main class="canvas">
    <section class="card card-front" aria-label="Business card front">
      <div class="brand-mark">
        <span class="square"></span>
        <span class="name">Linea</span>
      </div>
      <p class="front-web">www.lineaatelier.com</p>
    </section>

    <section class="card card-back" aria-label="Business card back">
      <div class="brand-lockup">
        <p class="title">LINEA ATELIER</p>
        <p class="byline">BY MARC DEVAUX</p>
      </div>
      <div class="person">
        <p class="person-name"><strong>DANIEL</strong> REYES</p>
        <p class="role">Graphic Designer</p>
      </div>
      <div class="contact">
        <p class="address">118 Harbor Lane<br>Westbrook 20417</p>
        <div class="lines">
          <p>555.0142.7731</p>
          <p>studio@lineaatelier.com</p>
          <p>www.lineaatelier.com</p>
        </div>
      </div>
    </section>
  </main>
</body>
</html>
```